Business Cards

We are an innovating group of real estate investors who buy beat up house's, fix them up, and resell them. We are in need of a business card that is catchy and stands out. We want it to say something like " We buy house's cash fast" Call us first

Industry/Entity Type

Business

Requirements
Must have
• Our logo which is updated

```html
<!DOCTYPE html>
<html lang="en">
<head>
<meta charset="utf-8">
<title>Keyfast Homes – Business Card</title>
<link rel="stylesheet" href="https://fonts.googleapis.com/css2?family=Questrial&display=swap">
<style>
  :root {
    --green: #6cbf3a;
    --green-deep: #4e9e2a;
    --purple: #8b2d8f;
    --purple-bright: #a232a6;
    --ink: #555555;
    --paper: #ffffff;
    --backdrop: #ececec;
  }
  * { box-sizing: border-box; margin: 0; padding: 0; }
  html, body { width: 1200px; height: 784px; overflow: hidden; }
  body {
    background: var(--backdrop);
    font-family: "Questrial", "Century Gothic", sans-serif;
    position: relative;
  }
  .card {
    position: absolute;
    top: 237px;
    width: 540px;
    height: 310px;
    box-shadow: 0 6px 18px rgba(0,0,0,0.15);
    overflow: hidden;
  }
  .card--back {
    left: 40px;
    background: linear-gradient(90deg, var(--green-deep) 0%, var(--green) 38%, #a48aa6 52%, var(--purple-bright) 68%, var(--purple) 100%);
  }
  .card--front { left: 620px; background: var(--paper); }

  .back-brand {
    position: absolute;
    left: 0; right: 0; top: 118px;
    text-align: center;
    font-size: 64px;
    color: rgba(255,255,255,0.12);
  }
  .tagline {
    position: absolute;
    left: 0; right: 0; top: 160px;
    text-align: center;
    color: #fff;
    font-size: 16px;
    letter-spacing: 4px;
    word-spacing: 4px;
  }

  .holder { position: absolute; right: 40px; top: 28px; text-align: right; }
  .holder__name { color: var(--green-deep); font-size: 16px; }
  .holder__role { color: var(--ink); font-size: 13px; margin-top: 2px; }

  .band { position: absolute; }
  .band--green { left: 0; top: 150px; width: 190px; height: 44px; background: var(--green); }
  .band--purple { left: 350px; top: 108px; width: 190px; height: 42px; background: var(--purple); }

  .brand {
    position: absolute;
    left: 190px; width: 160px; top: 137px;
    display: flex; align-items: center; justify-content: center; gap: 6px;
  }
  .brand__square { width: 12px; height: 12px; background: var(--green); }
  .brand__name { color: var(--purple); font-size: 17px; }

  .contacts {
    position: absolute; left: 40px; top: 214px;
    list-style: none; color: var(--ink); font-size: 15px; line-height: 19px;
  }
  .contacts li { display: flex; align-items: flex-start; gap: 8px; }
  .contacts svg { width: 16px; height: 16px; margin-top: 1px; flex: none; fill: var(--purple); }
</style>
</head>
<body>
  <section class="card card--back" aria-label="Card back">
    <div class="back-brand">Keyfast Homes</div>
    <p class="tagline">"We buy house's cash fast" Call us first</p>
  </section>

  <section class="card card--front" aria-label="Card front">
    <div class="holder">
      <div class="holder__name">Dane Porter</div>
      <div class="holder__role">Manager</div>
    </div>
    <div class="band band--green"></div>
    <div class="band band--purple"></div>
    <div class="brand">
      <span class="brand__square"></span>
      <span class="brand__name">Keyfast Homes</span>
    </div>
    <ul class="contacts">
      <li>
        <svg viewBox="0 0 24 24" aria-hidden="true"><path d="M6.6 10.8a15 15 0 0 0 6.6 6.6l2.2-2.2a1 1 0 0 1 1-.25 11.4 11.4 0 0 0 3.6.57 1 1 0 0 1 1 1V20a1 1 0 0 1-1 1A17 17 0 0 1 3 4a1 1 0 0 1 1-1h3.5a1 1 0 0 1 1 1c0 1.25.2 2.45.57 3.57a1 1 0 0 1-.25 1z"/></svg>
        <span>0400 555 218</span>
      </li>
      <li>
        <svg viewBox="0 0 24 24" aria-hidden="true"><path d="M12 2a10 10 0 1 0 0 20 10 10 0 0 0 0-20zm6.9 6h-2.9a15 15 0 0 0-1.4-3.6A8 8 0 0 1 18.9 8zM12 4c.8 1.2 1.5 2.5 1.9 4h-3.8c.4-1.5 1.1-2.8 1.9-4zM4.3 14a8 8 0 0 1 0-4h3.4a16 16 0 0 0 0 4zm.8 2h2.9a15 15 0 0 0 1.4 3.6A8 8 0 0 1 5.1 16zM8 8H5.1a8 8 0 0 1 4.3-3.6A15 15 0 0 0 8 8zm4 12c-.8-1.2-1.5-2.5-1.9-4h3.8c-.4 1.5-1.1 2.8-1.9 4zm2.3-6H9.7a14 14 0 0 1 0-4h4.6a14 14 0 0 1 0 4zm.3 5.6A15 15 0 0 0 16 16h2.9a8 8 0 0 1-4.3 3.6zm1.7-5.6a16 16 0 0 0 0-4h3.4a8 8 0 0 1 0 4z"/></svg>
        <span>www.keyfasthomes.com</span>
      </li>
      <li>
        <svg viewBox="0 0 24 24" aria-hidden="true"><path d="M3 6h18v12H3zm2 2v.5l7 4.5 7-4.5V8l-7 4.5z"/></svg>
        <span>dane@keyfasthomes.com</span>
      </li>
      <li>
        <svg viewBox="0 0 24 24" aria-hidden="true"><path d="M12 3 2 12h3v8h5v-5h4v5h5v-8h3z"/></svg>
        <span>Shop 9 Seaview Plaza, 140 Marlow<br>Parade Seaview NSW 2999</span>
      </li>
    </ul>
  </section>
</body>
</html>
```